One Page Magazine Ad for New Apartment in Calgary, AB Canada

We need a one page magazine ad for a new apartment community in Calgary, Alberta.

We pride ourselves in providing the highest level of customer service and the best amenities for our community.

COMMUNITY HIGHLIGHTS

- Brand new luxury apartment rental community in the exciting Calgary Beltline neighborhood
- 13 unique spacious floor plans fit for every lifestyle (1BR-1BATH, 2BR-1BATH & 2BR-2BATH)
- Professionally managed
- On-site staff during business hours to help you with any of your needs
- Pet-friendly community
- State of the art Fitness Facility
- 2 rooftop terraces outfitted with 8 Community Brimfield BBQs
- Great area for entertaining guests and a safe spot to take your dog out for some fresh air without leaving the building
- 2 resident lounges with multimedia suite, 60-inch TVs, Vexa Two, Silver Pin Arcade system, Poker table
- Great venues to host your next party, open 24/7 free to use and bookable by residents for free!
- Monthly resident events and parties hosted by the on-site staff
- Underground secured guest and resident parking available
- Electric Car Charging Stations
- Garbage & Recycling chutes on every floor
- Controlled Access/Building
- Gated Underground Parking Garage
- Adjacent to the Beltline neighborhood bike lane on 27th Avenue SW
- Elevators - Underground Secured Bike Storage and bike repair workstation
- On-site Maintenance
- Crate Keeper Package Management System
- Additional Storage Available
- Footsteps away from the local Fairmart Grocery and Fairmart Wine Store
- Minutes away from the new free leash dog park Wexley Park

APARTMENT AMENITIES

- Gourmet Kitchen with 4 piece Stainless Steel Appliances (Stove, Fridge, Microwave and Dishwasher)
- In suite dryer and washer
- Large Closets
- Patio/Balcony
- City and mountain views
- Ceramic Tile and Laminate Hardwood Flooring
- Quartz Counter-tops
- Roller Blinds for all Windows
- Walk-in Closets

For branding style, floor plans, amenities and photos please visit our website www.stayatthevorn.com

Target Market(s)

Young Adults and Recently Single Market

Industry/Entity Type

Real Estate

Font styles to use
Sans Serif

Colors
f37122

Requirements
Must have
• - Pictures of the community
• - Possibly use of a stock photo

```html
<!DOCTYPE html>
<html lang="en">
<head>
<meta charset="utf-8">
<title>New Apartment Community – Calgary, Alberta</title>
<link href="https://fonts.googleapis.com/css2?family=Open+Sans:wght@300;400;600;700&display=swap" rel="stylesheet">
<style>
  :root {
    --brand-orange: #f4560e;
    --panel-peach: #f7c598;
    --ink-dark: #222222;
    --ink-body: #3a3a3a;
    --paper: #ffffff;
    --frame-line: #1a1a1a;
  }
  * { margin: 0; padding: 0; box-sizing: border-box; }
  html, body { width: 923px; height: 1200px; overflow: hidden; background: var(--paper); }
  body { font-family: "Open Sans", Arial, sans-serif; color: var(--ink-body); }

  .ad { position: relative; width: 923px; height: 1200px; }
  .trim-frame { position: absolute; left: 0; top: 0; }

  .headline-band {
    position: absolute; left: 80px; top: 102px; width: 768px; height: 140px;
    background: var(--brand-orange); color: var(--paper);
  }
  .headline-new {
    position: absolute; left: 15px; top: 2px;
    font-size: 118px; font-weight: 600; letter-spacing: 2px; line-height: 136px;
  }
  .headline-title {
    position: absolute; left: 304px; top: 22px;
    font-size: 50px; font-weight: 600; line-height: 46px; letter-spacing: 1px;
  }
  .headline-title span { display: block; }
  .headline-title .line-two { margin-left: -5px; }
  .headline-city {
    position: absolute; left: 661px; top: 76px;
    font-size: 20px; font-weight: 400; line-height: 25px; letter-spacing: 0.5px;
  }

  .photo { position: absolute; left: 78px; width: 251px; height: 152px; }
  .photo-lounge { top: 254px; background: linear-gradient(160deg, #d9d9dc 0%, #8a8f9a 45%, #2a2f3d 75%, #a4553d 100%); }
  .photo-terrace { top: 424px; background: linear-gradient(180deg, #6b6e72 0%, #c9cbcc 40%, #e6e6e4 60%, #4b4b4b 100%); }
  .photo-bedroom { top: 599px; left: 79px; background: linear-gradient(120deg, #e4e7ea 0%, #c7ccd0 40%, #6f6458 70%, #eeeeee 100%); }

  .highlights-panel {
    position: absolute; left: 342px; top: 254px; width: 499px; height: 704px;
    background: var(--panel-peach);
  }
  .highlights-heading {
    position: absolute; left: 15px; top: 23px;
    font-size: 25.5px; font-weight: 700; color: var(--ink-dark); letter-spacing: 0.3px;
  }

  .bullet-list { list-style: none; position: absolute; }
  .bullet-list li {
    position: relative; font-size: 13px; font-weight: 300; line-height: 20.8px;
    padding-left: 13px; text-indent: -13px; color: var(--ink-body);
  }
  .bullet-list li::before {
    content: ""; position: absolute; left: -11px; top: 8px;
    width: 5px; height: 5px; border-radius: 50%; background: #333;
  }
  .highlights-list { left: 28px; top: 92px; width: 462px; }
  .highlights-list li::before { left: -11px; }

  .facilities-band {
    position: absolute; left: 80px; top: 780px; width: 248px; height: 42px;
    background: var(--brand-orange); color: var(--paper);
    font-size: 22px; font-weight: 600; line-height: 42px; padding-left: 12px; letter-spacing: 0.5px;
  }
  .facilities-list { left: 98px; top: 834px; width: 230px; }

  .contact-band {
    position: absolute; left: 342px; top: 975px; width: 499px; height: 109px;
    background: var(--brand-orange); color: var(--paper);
  }
  .brand-box {
    position: absolute; left: 39px; top: 9px; width: 141px; height: 88px;
    background: var(--paper); border: 1px solid #555;
    display: flex; align-items: center; justify-content: center; gap: 8px;
  }
  .brand-mark { width: 12px; height: 12px; background: var(--brand-orange); }
  .brand-name { font-size: 15px; font-weight: 400; letter-spacing: 3px; color: #444; }
  .contact-divider {
    position: absolute; left: 233px; top: 24px; height: 62px;
    border-left: 2px dotted rgba(255,255,255,0.85);
  }
  .contact-details {
    position: absolute; left: 264px; top: 18px;
    font-size: 12.3px; line-height: 16.8px; font-weight: 400;
  }
  .contact-details .strong { font-weight: 700; }
</style>
</head>
<body>
<main class="ad">
  <svg class="trim-frame" width="923" height="1200" aria-hidden="true">
    <rect x="24" y="38.5" width="871" height="1120" fill="none" stroke="var(--frame-line)" stroke-width="1.2"/>
    <g fill="none" stroke="var(--frame-line)" stroke-width="1">
      <path d="M24 51 H37 V38"/>
      <path d="M895 51 H882 V38"/>
      <path d="M24 1146 H37 V1158"/>
      <path d="M895 1146 H882 V1158"/>
    </g>
  </svg>

  <header class="headline-band">
    <div class="headline-new">NEW</div>
    <h1 class="headline-title"><span>APARTMENT</span><span class="line-two">COMMUNITY</span></h1>
    <div class="headline-city">CALGARY,<br>ALBERTA</div>
  </header>

  <div class="photo photo-lounge" role="img" aria-label="Resident lounge with poker table and colourful chairs"></div>
  <div class="photo photo-terrace" role="img" aria-label="Rooftop terrace with giant chess set and barbecues"></div>
  <div class="photo photo-bedroom" role="img" aria-label="Bright furnished bedroom with large windows"></div>

  <section class="highlights-panel">
    <h2 class="highlights-heading">THE BEAUTIFUL PLACE FOR LIVING</h2>
    <ul class="bullet-list highlights-list">
      <li>Brand new luxury apartment rental community in the exciting Calgary Beltline neighborhood</li>
      <li>13 unique spacious floor plans fit for every lifestyle (1BR-1BATH, 2BR-1BATH &amp; 2BR-2BATH)</li>
      <li>Professionally managed</li>
      <li>On-site staff during business hours to help you with any of your needs</li>
      <li>Pet-friendly community</li>
      <li>State of the art Fitness Facility</li>
      <li>2 rooftop terraces outfitted with 8 Community Brimfield BBQs</li>
      <li>Great area for entertaining guests and a safe spot to take your dog out for some fresh air without leaving the building</li>
      <li>2 resident lounges with multimedia suite, 60-inch TVs, Vexa Two, Silver Pin Arcade system, Poker table</li>
      <li>Great venues to host your next party, open 24/7 free to use and bookable by residents for free!</li>
      <li>Monthly resident events and parties hosted by the on-site staff</li>
      <li>Underground secured guest and resident parking available</li>
      <li>Electric Car Charging Stations</li>
      <li>Garbage &amp; Recycling chutes on every floor</li>
      <li>Controlled Access/Building</li>
      <li>Gated Underground Parking Garage</li>
      <li>Adjacent to the Beltline neighborhood bike lane on 27th Avenue SW</li>
      <li>Elevators - Underground Secured Bike Storage and bike repair workstation</li>
      <li>On-site Maintenance</li>
      <li>Crate Keeper Package Management System</li>
      <li>Additional Storage Available</li>
      <li>Footsteps away from the local Fairmart Grocery and Fairmart Wine Store</li>
      <li>Minutes away from the new free leash dog park Wexley Park</li>
    </ul>
  </section>

  <h2 class="facilities-band">FACILITIES</h2>
  <ul class="bullet-list facilities-list">
    <li>Gourmet Kitchen with 4 piece Stainless Steel Appliances (Stove, Fridge, Microwave and Dishwasher)</li>
    <li>In suite dryer and washer</li>
    <li>Large Closets</li>
    <li>Patio/Balcony</li>
    <li>City and mountain views</li>
    <li>Ceramic Tile and Laminate Hardwood Flooring</li>
    <li>Quartz Counter-tops</li>
    <li>Roller Blinds for all Windows</li>
    <li>Walk-in Closets</li>
  </ul>

  <footer class="contact-band">
    <div class="brand-box">
      <span class="brand-mark"></span>
      <span class="brand-name">THE VORN</span>
    </div>
    <div class="contact-divider"></div>
    <address class="contact-details" style="font-style: normal;">
      <div class="strong">+1 855-210-4783</div>
      <div>1480 9th Avenue SW</div>
      <div>Calgary, Alberta T2R 4K8</div>
      <div class="strong">www.stayatthevorn.com</div>
    </address>
  </footer>
</main>
</body>
</html>
```